Tarnowicz Family website redesign

Our family website tarnowicz.com has not been updated since 2010 and desperately needs a new look that's easy to edit. The new design needs to be able to accommodate all the current sections (some text, some photos/images/gallery), although not all need to be listed in top-level tabs.

The feel of the design should be fun and colorful without being childish or cartoonish (we're almost 60!). Also, we are math and engineering types so generally prefer geometric patterns/graphics.

I've attached some logos, graphics, and business card (done through ArtHarbor) that we use in other ways and especially like the green/red hummingbird, if it can be incorporated somehow.

Target Market(s)

Family and personal friends

Font styles to use
Sans Serif

Colors

Designer to choose colors to be used in the design.

Requirements
Must have
• Photo galleries, Contact Us form, password-protected section or page-by-page
Nice to have
• Blog posts (not sure we will use this but would be nice to have the option); social media links (Facebook, Instagram, Twitter)
Should not have
• E-commerce

```html
<!DOCTYPE html>
<html lang="en">
<head>
<meta charset="utf-8">
<title>Tarnowicz Family</title>
<link href="https://fonts.googleapis.com/css2?family=Tenor+Sans&family=Lato:wght@400;700&display=swap" rel="stylesheet">
<style>
:root{
  --page:#f4f4f4;
  --panel:#efefef;
  --blue:#0b4a96;
  --green:#2f6b12;
  --red:#d0111b;
  --ink:#222;
  --muted:#555;
  --bar:#262626;
  --white:#fff;
}
*{margin:0;padding:0;box-sizing:border-box}
html,body{width:1200px;height:3297px;overflow:hidden}
body{position:relative;background:var(--page);font-family:"Lato",sans-serif;color:var(--ink)}
.abs{position:absolute}
.display{font-family:"Tenor Sans",sans-serif}

.hero{left:0;top:0;width:1200px;height:622px;
  background:
    radial-gradient(ellipse 140px 90px at 600px 330px,rgba(255,214,150,.75),rgba(255,214,150,0) 70%),
    radial-gradient(ellipse 700px 120px at 600px 560px,rgba(0,0,0,.35),rgba(0,0,0,0) 70%),
    linear-gradient(180deg,#c3ced8 0%,#dfe4e8 14%,#eef0f1 24%,#d9d4cf 30%,#8d5a4c 36%,#7c4a3e 48%,#6e4236 58%,#3e4a2a 64%,#34402a 70%,#3b3b3d 76%,#2a2b2e 88%,#1b1f1a 100%)}
.menu-icon{left:118px;top:56px;width:26px;height:20px}
.menu-icon span{display:block;height:3px;background:#111;margin-bottom:5px}
.brand{left:500px;top:24px;width:200px;text-align:center}
.brand-dot{width:40px;height:40px;border-radius:50%;background:var(--green);margin:0 auto 10px}
.brand-name{font-family:"Tenor Sans",sans-serif;color:var(--blue);font-size:17px}
.pill{height:27px;border-radius:14px;color:var(--white);font-size:12px;font-weight:700;text-align:center;line-height:27px}
.btn-login{left:857px;top:54px;width:102px;background:var(--green)}
.btn-register{left:977px;top:54px;width:104px;background:var(--red)}
.welcome{left:0;top:448px;width:1200px;text-align:center;color:var(--white);font-size:29px;letter-spacing:1px;font-weight:400;text-shadow:0 1px 3px rgba(0,0,0,.5)}

.panel{background:var(--panel)}
.intro{left:18px;top:642px;width:496px;height:376px;display:flex;flex-direction:column;align-items:center;justify-content:center;text-align:center;font-size:12.5px;line-height:1.3;color:#333}
.intro p{margin-bottom:14px;width:272px}
.btn{background:var(--blue);color:var(--white);border-radius:14px;height:28px;line-height:28px;font-size:12px;text-align:center;font-weight:700}
.intro .btn{width:136px;margin-top:8px}
.caption{left:420px;top:1319px;width:382px;height:96px;background:var(--blue);color:var(--white);font-size:24px;text-align:center;display:flex;align-items:center;justify-content:center;line-height:1.4;letter-spacing:.5px}
.corner-mark{left:821px;top:1400px;width:16px;height:16px;background:#333;z-index:2}
.feature{display:flex;flex-direction:column;align-items:center;justify-content:center}
.feature h2{font-family:"Tenor Sans",sans-serif;font-weight:400;font-size:30px;margin-bottom:10px;letter-spacing:.5px}
.feature .btn{width:136px;height:27px;line-height:27px}

.section-title{width:1200px;left:0;text-align:center;font-family:"Tenor Sans",sans-serif;font-size:30px;font-weight:400}
.section-sub{width:1200px;left:0;text-align:center;font-size:12px;font-weight:700;letter-spacing:.5px}
.blog-card{width:290px}
.blog-img{height:183px;position:relative}
.date-badge{position:absolute;left:0;top:14px;width:32px;height:32px;background:var(--green);color:var(--white);font-size:11px;font-weight:700;line-height:1.05;padding:3px 4px}
.blog-title{font-family:"Tenor Sans",sans-serif;font-size:13px;font-weight:700;margin-top:14px;letter-spacing:.8px}
.blog-meta{display:flex;align-items:center;font-size:13px;color:#333;margin-top:5px}
.blog-meta .date{flex:1;display:flex;align-items:center;gap:10px}
.blog-meta .stat{display:flex;align-items:center;gap:3px;margin-left:16px}
.blog-text{font-size:13px;color:#444;line-height:1.4;margin-top:10px}
.read-more{font-size:13px;margin-top:16px;display:flex;align-items:center;gap:4px}

.label{font-size:13px;color:#333}
.footer-text{font-size:13px;line-height:1.35;color:#222}
.footer-head{font-size:12px;font-weight:700;letter-spacing:.5px}
.footer-rule{width:40px;height:2px;background:#222;margin:10px 0 14px}
.footer-list{list-style:none;font-size:12px;line-height:1.55}
.footer-list li::before{content:"› "}
.contact-row{display:flex;gap:8px;font-size:13px;line-height:1.35;margin-bottom:6px}
.subscribe{display:flex;align-items:center;margin-top:12px}
.subscribe input{width:180px;height:28px;border:none;background:var(--white);font:italic 11px "Lato",sans-serif;padding-left:12px;color:#333}
.subscribe .go{width:36px;height:28px;border-radius:0 14px 14px 0;background:var(--blue);display:flex;align-items:center;justify-content:center}
.bottom-bar{left:0;top:3246px;width:1200px;height:51px;background:var(--bar);color:var(--white);font-size:13px}
.legal{left:120px;top:17px}
.social{right:120px;top:13px;display:flex;gap:14px}
.social span{width:26px;height:26px;border-radius:50%;background:var(--white);box-shadow:inset 0 0 0 7px var(--white),inset 0 0 0 9px #3a3a3a;display:block}

.ph-family{background:
  radial-gradient(ellipse 260px 150px at 360px 250px,rgba(60,45,45,.75),rgba(60,45,45,0) 75%),
  radial-gradient(ellipse 90px 120px at 590px 170px,rgba(240,240,235,.9),rgba(240,240,235,0) 80%),
  linear-gradient(100deg,#dcdcd6 0%,#c9c6c0 30%,#a39a94 55%,#8f847c 75%,#e6e6e0 100%)}
.ph-wedding{background:
  radial-gradient(ellipse 90px 170px at 120px 230px,rgba(250,248,244,.95),rgba(250,248,244,0) 80%),
  radial-gradient(ellipse 110px 160px at 230px 220px,rgba(245,242,236,.9),rgba(245,242,236,0) 80%),
  linear-gradient(160deg,#d9d3c7 0%,#c8bca8 40%,#6d6458 75%,#2f2b28 100%)}
.ph-garden{background:
  radial-gradient(ellipse 200px 90px at 190px 200px,rgba(30,35,55,.8),rgba(30,35,55,0) 80%),
  linear-gradient(180deg,#8aa56c 0%,#6f8a57 35%,#4e5a4a 60%,#2d3445 100%)}
.ph-portrait{position:absolute}
</style>
</head>
<body>

<header>
  <div class="abs hero" role="img" aria-label="Large brick family house with white columns and lit windows at dusk"></div>
  <div class="abs menu-icon"><span></span><span></span><span></span></div>
  <div class="abs brand"><div class="brand-dot"></div><div class="brand-name">Dana &amp; Tomek</div></div>
  <div class="abs pill btn-login">Login</div>
  <div class="abs pill btn-register">Register</div>
  <h1 class="abs welcome display">Welcome to the Tarnowicz Family</h1>
</header>

<main>
  <section class="abs panel intro">
    <p>I've been busy! Our 2010 card and letter<br>are now posted!<br>Woo-hoo!!</p>
    <p>All of our Christmas picture cards<br>(starting in the year we were married, 1981)<br>are now available. All Holiday letters (starting<br>in 1989) are now available.</p>
    <div class="btn">Read More</div>
  </section>
  <div class="abs ph-family" style="left:532px;top:642px;width:650px;height:376px" role="img" aria-label="Family portrait of six on a staircase"></div>

  <div class="abs ph-wedding" style="left:18px;top:1037px;width:384px;height:378px" role="img" aria-label="Wedding couple cutting their cake"></div>
  <div class="abs ph-garden" style="left:420px;top:1037px;width:382px;height:282px" role="img" aria-label="Family group photo in a garden"></div>
  <div class="abs caption display">Merry christmas and a<br>happy new year to you !</div>
  <section class="abs panel feature" style="left:822px;top:1037px;width:360px;height:378px">
    <h2>Christmas Cards</h2><div class="btn">View All</div>
  </section>
  <div class="abs corner-mark"></div>

  <section class="abs panel feature" style="left:18px;top:1435px;width:347px;height:510px">
    <h2>Photo Album</h2><div class="btn">View All</div>
  </section>
  <div class="abs" style="left:382px;top:1439px;width:260px;height:244px;background:radial-gradient(ellipse 80px 100px at 130px 110px,#e6cdb8,rgba(230,205,184,0) 80%),linear-gradient(180deg,#b9b6b0 0%,#a8a49c 60%,#2c3548 100%)" role="img" aria-label="Childhood school portrait"></div>
  <div class="abs" style="left:659px;top:1439px;width:260px;height:244px;background:radial-gradient(ellipse 80px 100px at 130px 110px,#e9cfae,rgba(233,207,174,0) 80%),linear-gradient(180deg,#ecdcb4 0%,#dcc596 60%,#5a6a88 100%)" role="img" aria-label="Childhood school portrait"></div>
  <div class="abs" style="left:938px;top:1439px;width:244px;height:244px;background:radial-gradient(ellipse 80px 100px at 122px 110px,#dcb393,rgba(220,179,147,0) 80%),linear-gradient(180deg,#86b8e0 0%,#5f95c8 60%,#1f4f8a 100%)" role="img" aria-label="Childhood school portrait"></div>
  <div class="abs" style="left:382px;top:1703px;width:260px;height:244px;background:radial-gradient(ellipse 80px 100px at 130px 120px,#e3c4a6,rgba(227,196,166,0) 80%),linear-gradient(180deg,#8fa6c6 0%,#6a84aa 60%,#e4e2dc 100%)" role="img" aria-label="Childhood school portrait"></div>
  <div class="abs" style="left:659px;top:1703px;width:260px;height:244px;background:radial-gradient(ellipse 80px 100px at 130px 120px,#e6c6aa,rgba(230,198,170,0) 80%),linear-gradient(180deg,#cfdcea 0%,#aebccc 60%,#8aa2a0 100%)" role="img" aria-label="Childhood school portrait"></div>
  <div class="abs" style="left:938px;top:1703px;width:244px;height:244px;background:radial-gradient(ellipse 80px 100px at 122px 120px,#c89a78,rgba(200,154,120,0) 80%),linear-gradient(180deg,#6f8cc0 0%,#4a659a 60%,#1e2c4c 100%)" role="img" aria-label="Childhood school portrait"></div>

  <h2 class="abs section-title" style="top:2008px">Our Blogs</h2>
  <p class="abs section-sub" style="top:2052px">Lorem Ipsum is simply dummy text.</p>

  <article class="abs blog-card" style="left:121px;top:2103px">
    <div class="blog-img" style="background:radial-gradient(ellipse 70px 85px at 145px 85px,#d9b08e,rgba(217,176,142,0) 80%),linear-gradient(180deg,#b08e7c 0%,#8c6a5c 60%,#eae6e0 100%)" role="img" aria-label="Portrait of a woman"><div class="date-badge">20<br>Mar</div></div>
    <div class="blog-title">Blog Title Heading</div>
    <div class="blog-meta"><span class="date"><svg width="10" height="10"><rect x="1" y="2" width="8" height="7" fill="none" stroke="#333"/></svg>Nov 01, 2018</span><span class="stat">♡20</span><span class="stat">♡ 12</span></div>
    <p class="blog-text">Lorem Ipsum is simply dummy text of the matter and typesetting in industry.</p>
    <div class="read-more">Read More..<svg width="9" height="9"><circle cx="4.5" cy="4.5" r="3.5" fill="none" stroke="#333"/></svg></div>
  </article>
  <article class="abs blog-card" style="left:457px;top:2103px">
    <div class="blog-img" style="background:radial-gradient(ellipse 70px 85px at 145px 90px,#d8ab88,rgba(216,171,136,0) 80%),linear-gradient(180deg,#8a8680 0%,#6e6a64 60%,#8c8cb4 100%)" role="img" aria-label="Portrait of a young man"><div class="date-badge">21<br>Mar</div></div>
    <div class="blog-title">Blog Title Heading</div>
    <div class="blog-meta"><span class="date"><svg width="10" height="10"><rect x="1" y="2" width="8" height="7" fill="none" stroke="#333"/></svg>Nov 15, 2018</span><span class="stat">♡20</span><span class="stat">♡ 12</span></div>
    <p class="blog-text">Lorem Ipsum is simply dummy text of the matter and typesetting in industry.</p>
    <div class="read-more">Read More..<svg width="9" height="9"><circle cx="4.5" cy="4.5" r="3.5" fill="none" stroke="#333"/></svg></div>
  </article>
  <article class="abs blog-card" style="left:791px;top:2103px">
    <div class="blog-img" style="background:radial-gradient(ellipse 70px 85px at 145px 90px,#e2b89a,rgba(226,184,154,0) 80%),linear-gradient(180deg,#8cbce2 0%,#6aa0d0 60%,#b0806a 100%)" role="img" aria-label="Portrait of a young woman"><div class="date-badge">21<br>Mar</div></div>
    <div class="blog-title">Blog Title Heading</div>
    <div class="blog-meta"><span class="date"><svg width="10" height="10"><rect x="1" y="2" width="8" height="7" fill="none" stroke="#333"/></svg>April10, 2018</span><span class="stat">♡20</span><span class="stat">♡12</span></div>
    <p class="blog-text">Lorem Ipsum is simply dummy text of the matter and typesetting in industry.</p>
    <div class="read-more">Read More..<svg width="9" height="9"><circle cx="4.5" cy="4.5" r="3.5" fill="none" stroke="#333"/></svg></div>
  </article>
  <div class="abs btn" style="left:534px;top:2473px;width:136px;height:30px;line-height:30px">View More</div>

  <h2 class="abs section-title" style="top:2565px;font-size:28px">Quick Contact</h2>
  <form>
    <label class="abs label" style="left:314px;top:2641px">Name</label>
    <label class="abs label" style="left:631px;top:2641px">Phone</label>
    <label class="abs label" style="left:314px;top:2682px">Email</label>
    <label class="abs label" style="left:317px;top:2731px">Message</label>
    <div class="abs btn" style="left:538px;top:2842px;width:128px;height:29px;line-height:29px">Send</div>
  </form>
</main>

<footer>
  <div class="abs" style="left:121px;top:2972px;width:220px">
    <div style="width:40px;height:40px;border-radius:50%;background:var(--green);margin:0 0 6px 22px"></div>
    <div class="display" style="color:var(--blue);font-size:17px;margin-bottom:6px">Dana &amp; Tomek</div>
    <p class="footer-text">Lorem Ipsum is simply dummy text of the printing and typesetting ind ustry. Lorem Ipsum dummy text ever sinc in the 1500..</p>
  </div>
  <div class="abs" style="left:455px;top:3006px">
    <div class="footer-head">Quick Link</div><div class="footer-rule"></div>
    <ul class="footer-list"><li>Home</li><li>Christmas Cards</li><li>Kids</li><li>What's New</li><li>Fun &amp; Games</li><li>Contact us</li></ul>
  </div>
  <div class="abs" style="left:644px;top:3006px;width:200px">
    <div class="footer-head">Contact Us</div><div class="footer-rule"></div>
    <div class="contact-row"><svg width="12" height="12" viewBox="0 0 12 12"><path d="M2 1h3l1 3-2 1a7 7 0 0 0 3 3l1-2 3 1v3c-6 1-10-3-9-9z" fill="#222"/></svg>Phone: 123 456 7890</div>
    <div class="contact-row"><svg width="12" height="12"><rect x="1" y="3" width="10" height="7" fill="#222"/></svg>info@danatomek.com</div>
    <div class="contact-row"><svg width="12" height="14" viewBox="0 0 12 14"><path d="M6 1a4 4 0 0 1 4 4c0 3-4 8-4 8S2 8 2 5a4 4 0 0 1 4-4z" fill="#222"/><circle cx="6" cy="5" r="1.5" fill="#fff"/></svg>Address : 12th Street,<br>City ,Usa</div>
  </div>
  <div class="abs" style="left:862px;top:3006px;width:230px">
    <div class="footer-head">Subscribe</div><div class="footer-rule"></div>
    <p class="footer-text">Lorem Ipsum is simply dummy and typesetting industry</p>
    <div class="subscribe"><input value="Your Email"><span class="go"><svg width="14" height="14" viewBox="0 0 14 14"><path d="M1 7l12-6-4 12-2-5z" fill="#fff"/></svg></span></div>
  </div>
  <div class="abs bottom-bar">
    <div class="abs legal">Privacy policy - Legal mentions - Terms and Conditions -</div>
    <div class="abs social"><span></span><span></span><span></span><span></span></div>
  </div>
</footer>

</body>
</html>
```